New Business Card for Innovative Tool Company

We need a new design of business card for our florida based tool manufacturing company. I will attach 2 files that we use for our logo, use whichever you feel works best for the card. Main colours are as per logo, and we can use different shades of black/white/grey for the background.

Contact Information for Business Card

Name/Jobtitle/cell
Corvalen Tools
Suite 212c
4316 Marrowdale Pkw
Orlando, FL32847
USA
name@corvaleninc.example
www.corvaleninc.example

Font styles to use
Sans Serif

Colors

Designer to choose colors to be used in the design.

Requirements
Must have
• Icons for Plazaro, Chirpet, Snapvale, Findlo & Vidstream

```html
<!DOCTYPE html>
<html lang="en">
<head>
<meta charset="UTF-8">
<title>Corvalen Tools – Business Card</title>
<link href="https://fonts.googleapis.com/css2?family=Work+Sans:wght@400;500;700&display=swap" rel="stylesheet">
<style>
  :root {
    --page: #d6d6d6;
    --card: #2b2b2b;
    --accent: #f2ea32;
    --ink: #ffffff;
    --ink-soft: #e6e6e6;
    --disc: #6e6e6e;
    --ring: #d9d9d9;
    --halo: #4a4a4a;
  }
  * { box-sizing: border-box; margin: 0; padding: 0; }
  html, body { width: 1200px; height: 900px; overflow: hidden; }
  body {
    background: var(--page);
    font-family: "Work Sans", Arial, sans-serif;
    display: flex;
    flex-direction: column;
    align-items: center;
    justify-content: center;
    gap: 56px;
  }
  .card {
    width: 580px;
    height: 331px;
    background: var(--card);
    position: relative;
    box-shadow: 0 10px 24px rgba(0,0,0,0.25);
  }
  .card--front { border-left: 5px solid var(--accent); border-bottom: 5px solid var(--accent); display: flex; align-items: center; }
  .card--back { border-bottom: 5px solid var(--accent); display: flex; align-items: center; justify-content: center; }

  .brand { width: 300px; display: flex; flex-direction: column; align-items: center; gap: 14px; }
  .brand__mark { width: 74px; height: 74px; border-radius: 50%; border: 1.5px solid var(--accent); }
  .brand__name { color: var(--accent); font-weight: 700; font-size: 26px; letter-spacing: 0.5px; text-transform: uppercase; }

  .divider { width: 2px; height: 160px; background: var(--ink-soft); }

  .contact { padding-left: 26px; padding-right: 14px; color: var(--ink); }
  .contact__name { color: var(--accent); font-weight: 500; font-size: 22px; text-transform: uppercase; letter-spacing: 0.5px; }
  .contact__title { font-size: 14px; margin-bottom: 12px; }
  .contact__address { font-size: 14px; line-height: 1.35; margin-bottom: 8px; }
  .contact__list { list-style: none; font-size: 14px; line-height: 1.5; }
  .contact__list li { display: flex; align-items: center; gap: 8px; }
  .contact__list svg { width: 12px; height: 12px; flex: none; }
  .contact__hl { color: var(--accent); }

  .social { list-style: none; display: flex; flex-wrap: wrap; gap: 4px 10px; margin-top: 10px; max-width: 230px; font-size: 11px; color: var(--ink-soft); }
  .social li { display: flex; align-items: center; gap: 4px; }
  .social__dot { width: 8px; height: 8px; border-radius: 50%; background: var(--accent); flex: none; }

  .emblem {
    width: 150px; height: 150px; border-radius: 50%;
    background: var(--disc);
    border: 4px solid var(--ring);
    box-shadow: 0 0 0 6px var(--halo);
  }
</style>
</head>
<body>

<section class="card card--front">
  <div class="brand">
    <div class="brand__mark"></div>
    <div class="brand__name">Corvalen Tools</div>
  </div>
  <div class="divider"></div>
  <div class="contact">
    <h1 class="contact__name">Daniel Hartwell</h1>
    <p class="contact__title">Director</p>
    <p class="contact__address">Suite 212c<br>4316 Marrowdale Pkw<br>Orlando, FL32847 USA</p>
    <ul class="contact__list">
      <li>
        <svg viewBox="0 0 24 24" fill="var(--accent)"><path d="M6.6 10.8a15 15 0 0 0 6.6 6.6l2.2-2.2c.3-.3.7-.4 1-.2 1.1.4 2.3.6 3.6.6.6 0 1 .4 1 1V20c0 .6-.4 1-1 1A17 17 0 0 1 3 4c0-.6.4-1 1-1h3.5c.6 0 1 .4 1 1 0 1.3.2 2.5.6 3.6.1.3 0 .7-.2 1z"/></svg>
        +330 5814-2073
      </li>
      <li>
        <svg viewBox="0 0 24 24" fill="none" stroke="var(--accent)" stroke-width="2.2"><rect x="3" y="5" width="18" height="14" rx="1"/><path d="M3 6l9 7 9-7"/></svg>
        name@corvaleninc.example
      </li>
      <li>
        <svg viewBox="0 0 24 24" fill="none" stroke="var(--accent)" stroke-width="2"><circle cx="12" cy="12" r="9"/><path d="M3 12h18M12 3c3 3 3 15 0 18M12 3c-3 3-3 15 0 18"/></svg>
        <span>www.<span class="contact__hl">corvaleninc</span>.example</span>
      </li>
    </ul>
    <ul class="social">
      <li><span class="social__dot"></span>Plazaro</li>
      <li><span class="social__dot"></span>Chirpet</li>
      <li><span class="social__dot"></span>Snapvale</li>
      <li><span class="social__dot"></span>Findlo</li>
      <li><span class="social__dot"></span>Vidstream</li>
    </ul>
  </div>
</section>

<section class="card card--back">
  <div class="emblem" role="img" aria-label="Corvalen Tools emblem"></div>
</section>

</body>
</html>
```